Fiber Optic Internet flyer promotion Winter 2016-2017

I am looking for a marketing flyer that will not be folded, single sided that will advertise a Fiber Optic internet promotion that we are currently running.

The design should be clean, flow well, quickly grab attention, and if a very few short seconds list what the promotion is, and direct them to contact us.

It needs to list a few features of the promotion, but does not need to be in this order and should flow well with the flyer
1.) Fiber Optic Internet
2.) 100 Mbits for $140 /month or 150 Mbits for $190 /month
3.) Free construction cost up to $10,000, limited funds available.
4.) Limited time offer. Must commit before funds run out.

(555) 274-3916, www.kelvoranet.example

Target Market(s)

Small to large business

Industry/Entity Type

Internet Service Provider

Requirements
Must have
• Eye catching appeal. Quickly convey the message of the promotion and our company name and phone number.
Should not have
• Our company is primarily a wireless ISP. This promotion is all about Fiber Optic. I do not want to draw attention to the "wireless" portion of our business with this flyer.

```html
<!DOCTYPE html>
<html lang="en">
<head>
<meta charset="utf-8">
<title>Fiber Optic Internet Flyer</title>
<link href="https://fonts.googleapis.com/css2?family=Noto+Serif:ital,wght@1,700&family=Open+Sans:wght@600;700&family=Roboto:wght@700;900&display=swap" rel="stylesheet">
<style>
  :root{
    --mat:#d6d7d9;
    --navy:#27357c;
    --navy-deep:#1e2a66;
    --sky:#5cc3ea;
    --red:#d2202f;
    --gold:#f6d31a;
    --white:#ffffff;
    --ink:#111111;
  }
  *{margin:0;padding:0;box-sizing:border-box}
  html,body{width:924px;height:1200px;overflow:hidden;background:var(--mat)}
  .flyer{position:absolute;left:107px;top:63px;width:723px;height:1074px;overflow:hidden;background:var(--navy)}
  .flyer-art{position:absolute;inset:0;width:723px;height:1074px}
  .headline{position:absolute;left:32px;top:30px;font-family:"Noto Serif",Georgia,serif;font-style:italic;font-weight:700;line-height:1}
  .headline-main{display:block;color:var(--gold);font-size:62px}
  .headline-sub{display:block;color:var(--red);font-size:44px;margin-top:8px}
  .brand{position:absolute;left:415px;top:165px;display:flex;align-items:center;gap:12px;font-family:"Open Sans",Arial,sans-serif;font-weight:700;font-size:30px;color:var(--navy);letter-spacing:1px}
  .brand-mark{width:26px;height:26px;background:var(--navy)}
  .offer-card{position:absolute;left:32px;top:450px;width:278px;height:481px;background:var(--gold);border:3px solid var(--ink);border-radius:26px;padding:37px 14px 0 16px;font-family:"Open Sans",Arial,sans-serif}
  .offer-title{color:var(--navy);font-weight:700;font-size:19px;text-align:center;letter-spacing:.2px}
  .offer-rule{width:112px;height:2px;background:var(--red);margin:14px auto 16px}
  .offer-list{list-style:none}
  .offer-list li{position:relative;padding-left:15px;color:var(--red);font-weight:600;font-size:20px;line-height:26px;margin-bottom:39px;white-space:nowrap;letter-spacing:-.2px}
  .offer-list li::before{content:"";position:absolute;left:0;top:10px;width:7px;height:7px;border-radius:50%;background:var(--red)}
  .offer-rule.bottom{margin-top:-8px}
  .phone{position:absolute;left:336px;top:782px;font-family:"Roboto",Arial,sans-serif;font-weight:700;font-size:37px;color:var(--navy)}
  .website{position:absolute;right:42px;top:1000px;font-family:"Roboto",Arial,sans-serif;font-weight:700;font-size:35px;color:var(--white)}
</style>
</head>
<body>
<main class="flyer">
  <svg class="flyer-art" viewBox="0 0 723 1074" xmlns="http://www.w3.org/2000/svg">
    <defs>
      <radialGradient id="globe-tones" cx="0.71" cy="0.48" r="0.62">
        <stop offset="0" stop-color="#8fd3ff"/>
        <stop offset="0.18" stop-color="#4aa4ec"/>
        <stop offset="0.42" stop-color="#2170cf"/>
        <stop offset="0.75" stop-color="#124a9e"/>
        <stop offset="1" stop-color="#0a2466"/>
      </radialGradient>
      <radialGradient id="cable-tones" cx="0.5" cy="0.5" r="0.5">
        <stop offset="0" stop-color="#7d8a86"/>
        <stop offset="0.45" stop-color="#b9c7bf" stop-opacity="0.8"/>
        <stop offset="1" stop-color="#ffffff" stop-opacity="0"/>
      </radialGradient>
    </defs>
    <rect width="723" height="1074" fill="var(--navy)"/>
    <rect class="hero-photo" x="0" y="240" width="723" height="500" fill="url(#globe-tones)" role="img" aria-label="Photo of a glowing digital globe with streaks of fiber optic light"/>
    <path class="top-band" d="M0,270 C250,200 490,95 723,60 L723,80 C490,115 250,220 0,290 Z" fill="var(--sky)"/>
    <path class="top-swoosh" d="M0,290 C250,220 490,115 723,80 L723,255 C490,270 250,300 0,365 Z" fill="var(--white)"/>
    <ellipse class="cable-illustration" cx="200" cy="252" rx="110" ry="62" transform="rotate(-25 200 252)" fill="url(#cable-tones)" role="img" aria-label="Illustration of a fiber optic cable with fanned-out colored strands"/>
    <path class="top-accent" d="M0,365 C250,300 490,270 723,255 L723,266 C490,284 250,322 0,392 Z" fill="var(--red)"/>
    <rect class="divider" x="0" y="737" width="723" height="8" fill="var(--navy-deep)"/>
    <rect class="contact-band" x="0" y="745" width="723" height="329" fill="var(--sky)"/>
    <path class="bottom-accent" d="M0,985 C250,972 560,915 723,832 L723,850 C560,940 250,1000 0,1018 Z" fill="var(--red)"/>
    <path class="bottom-base" d="M0,1010 C250,990 560,935 723,848 L723,1074 L0,1074 Z" fill="var(--navy)"/>
  </svg>

  <h1 class="headline">
    <span class="headline-main">Fiber Optic</span>
    <span class="headline-sub">Internet</span>
  </h1>

  <div class="brand"><span class="brand-mark"></span>KELVORA NET</div>

  <section class="offer-card">
    <h2 class="offer-title">FIBER OPTIC INTERNET</h2>
    <div class="offer-rule"></div>
    <ul class="offer-list">
      <li>100 Mbits for $140<br>/month or 150 Mbits<br>for $190 /month</li>
      <li>Free construction cost<br>up to $10,000, limited<br>funds available.</li>
      <li>Limited time offer.<br>Must commit before<br>funds run out.</li>
    </ul>
    <div class="offer-rule bottom"></div>
  </section>

  <p class="phone">Tel; (555) 274-3916</p>
  <p class="website">www.kelvoranet.example</p>
</main>
</body>
</html>
```